Brochure for Community-Based Therapy Company

Will be given out to patients, doctors, case managers. We are redesigning our marketing materials and would like a design for a brochure. We provide therapy to individuals who have been injured in car accidents or on the job. We provide occupational therapy, speech therapy and psychotherapy. We would like the brochure to utilize our corporate ID and color scheme that we are using for our other materials (see attached letterhead and logo).

Stock photos that are used should stay away from images of outpatient or hospital settings, stay away from photos with obvious disabilities (wheelchairs, learning to walk, etc), and nothing that looks like physical therapy, as we don't provide physical therapy only OT, Speech and psychotherapy. Would prefer to not have people wearing masks, as we will use this beyond the pandemic. Also, our staff wears business casual clothing so would prefer photos that the individuals are not wearing scrubs or other medical attire (lab coats, etc).

Target Market(s)

Patients, Physicians/Doctors, Case Managers

Industry/Entity Type

Healthcare

Requirements
Must have
• Prefer a booklet format but doesn't have to be 8.5 inch by 11 inch (can be a little smaller).

```html
<!DOCTYPE html>
<html lang="en">
<head>
<meta charset="utf-8">
<title>Northfield Recovery Partners – Brochure Spread</title>
<link href="https://fonts.googleapis.com/css2?family=Montserrat:wght@600;700;800&family=Open+Sans:ital,wght@0,400;0,600;0,700;1,400;1,600&display=swap" rel="stylesheet">
<style>
  :root{
    --backdrop:#2a2a2a;
    --paper:#ffffff;
    --paper-shade:#eeeeee;
    --sage:#8ea394;
    --sage-dark:#74897a;
    --sage-light:#b3c2b7;
    --ink:#3a3a3a;
    --heading:#2c2c2c;
  }
  *{box-sizing:border-box;margin:0;padding:0}
  html,body{width:1200px;height:833px;overflow:hidden;background:var(--backdrop)}
  body{font-family:"Open Sans",Arial,sans-serif;color:var(--ink)}
  .spread{position:absolute;left:20px;top:22px;width:1160px;height:789px;display:flex;box-shadow:0 10px 30px rgba(0,0,0,.5)}
  .page{width:580px;height:789px;padding:30px 34px 24px;position:relative;overflow:hidden}
  .page--left{background:linear-gradient(90deg,var(--paper) 0%,var(--paper) 85%,var(--paper-shade) 100%)}
  .page--right{background:linear-gradient(90deg,var(--paper-shade) 0%,var(--paper) 12%,var(--paper) 100%)}
  .section-title{font-family:"Montserrat",Arial,sans-serif;font-weight:800;font-size:13px;letter-spacing:3.2px;text-transform:uppercase;color:var(--heading);padding-bottom:3px;border-bottom:1px solid var(--sage);margin-bottom:5px}
  .section-title--large{font-size:15px;letter-spacing:4px}
  p{font-size:8.4px;line-height:1.42;margin-bottom:5px;text-align:justify}
  .statement{font-style:italic}
  .section{margin-bottom:9px}
  .banner{background:var(--sage);color:#fff;font-family:"Open Sans",Arial,sans-serif;font-weight:700;font-style:italic;font-size:10px;padding:5px 16px;border-radius:0 14px 14px 0;margin:4px 0 9px -34px;padding-left:50px}
  .banner--narrow{width:70%}
  .factors{display:grid;grid-template-columns:1fr 1fr;column-gap:22px;margin-bottom:6px}
  .factor h3{font-family:"Montserrat",Arial,sans-serif;font-weight:700;font-size:9.6px;color:var(--heading);margin-bottom:2px;display:flex;gap:5px;align-items:flex-start}
  .factor{margin-bottom:7px}
  .tick{flex:none;width:9px;height:9px;border:1px solid var(--sage);border-radius:50%;position:relative;margin-top:1px;display:inline-block}
  .tick::after{content:"";position:absolute;left:2.3px;top:1px;width:2.5px;height:4px;border:solid var(--sage);border-width:0 1px 1px 0;transform:rotate(45deg)}
  .tick--light{border-color:#e6ece7}
  .tick--light::after{border-color:#e6ece7}
  .check-list{list-style:none}
  .check-list li{display:flex;gap:5px;align-items:flex-start;font-size:8.4px;line-height:1.38;margin-bottom:4px}
  .diagnoses{background:linear-gradient(135deg,var(--sage-light),var(--sage) 45%,var(--sage-dark));color:#fff;border-radius:0 0 16px 0;margin:6px -34px 12px;padding:12px 22px 14px 40px;display:grid;grid-template-columns:1fr 1.1fr 0.9fr;column-gap:14px}
  .diagnoses h4{grid-column:1 / 3;font-family:"Montserrat",Arial,sans-serif;font-weight:700;font-size:10.5px;margin-bottom:6px}
  .diagnoses .check-list li{font-size:8.2px;margin-bottom:3px}
  .funding{grid-column:3;grid-row:1 / 3;border-left:1px solid rgba(255,255,255,.8);padding-left:12px;align-self:end}
  .funding h4{font-size:10.5px;margin-bottom:6px}
  .sub-title{font-family:"Montserrat",Arial,sans-serif;font-weight:700;font-size:10px;color:var(--heading);margin:4px 0 3px}
  .services{display:grid;grid-template-columns:1fr 1fr;column-gap:22px;margin-bottom:8px}
  .services .check-list li{font-size:8.2px}
</style>
</head>
<body>
<main class="spread">
  <section class="page page--left">
    <div class="section">
      <h2 class="section-title section-title--large">Mission Statement</h2>
      <p class="statement">Our mission is to provide high quality therapy that allows the people we serve to achieve an optimal level of functioning and to improve their quality of life.</p>
    </div>
    <div class="section">
      <h2 class="section-title section-title--large">Vision Statement</h2>
      <p class="statement">To be a recognized leader in functional rehabilitation to individuals with a variety of diagnoses in the home and community-based setting with an emphasis on goal-directed individual rehabilitation for addressing safety, skill building, independence, and cognitive and physical recovery.</p>
    </div>
    <div class="section">
      <h2 class="section-title section-title--large">Who We Are</h2>
      <p>For over 25 years, our company has been using evidence-based principles of rehabilitation to assist patients with their recovery. We are out in the real world with patients every day, helping them to get their lives back. Our goal is to provide functional home and community-based therapy to provide patient-centered holistic therapy with a state-of-the-art approach. Using the patient's natural environment such as their home, community or workplace allows us to attain measurable outcomes that turn even small successes into something bigger.</p>
    </div>
    <div class="banner">Finding success in the rehabilitative process relies on certain key factors:</div>
    <div class="factors">
      <div>
        <div class="factor">
          <h3><span class="tick"></span>Getting to Know You:</h3>
          <p>We do not set goals that are important to us, but rather, we set goals that are important to you. We take input from you, and the people you trust like your physician, case manager or perhaps a trusted family member to identify your needs and then make a plan that is best suited for success.</p>
        </div>
        <div class="factor">
          <h3><span class="tick"></span>Creating and Implementing a Customized Rehabilitation Plan:</h3>
          <p>After the evaluation protocols are completed, a system of long-term and short-term goals are developed using our team approach. This allows for therapy to be tailored to your individual needs. A plan of care is developed and implemented based on your goals and the results of the evaluation.</p>
        </div>
      </div>
      <div>
        <div class="factor">
          <h3><span class="tick"></span>Comprehensive Evaluation:</h3>
          <p>We begin with an in-depth assessment with comprehensive evaluation protocols to determine your current level of functioning and how it compares to your prior level of functioning. We can then identify the areas that have been impacted and begin addressing them.</p>
        </div>
        <div class="factor">
          <h3><span class="tick"></span>Focus on Accomplishments (Breaking Down Success):</h3>
          <p>In order to facilitate progress toward patient goals, our therapy is most effective with consistent therapy appointments and repetition across therapy disciplines, which maximizes carry over outside of therapy.</p>
        </div>
      </div>
    </div>
    <div class="banner banner--narrow">Why Our Approach to Brain Injury is Unique</div>
    <p>In more traditional therapy settings such as programs using outpatient models, attempts are made to simulate functional activities, combined with more structured tasks, all performed within their clinic environment. However, the inability to generalize learning has been shown to be a reoccurring difficulty for individuals with Traumatic Brain Injury and can often manifest in cognitive inflexibility, which makes carryover of their learned skills to the real world a challenge.</p>
    <p>Community-based treatment circumvents this difficulty by conducting therapy in the person's home, school, workplace, or other settings within their community, such as a grocery store or at a post office. Clinicians are therefore able to witness first hand where a task is experiencing success or breaking down and can structure treatment accordingly. This allows for greater natural development of functional skills, with generalization issues no longer an obstacle toward meeting treatment goals.</p>
    <p>At Northfield Recovery Partners we are committed to helping people recover their cognitive, physical and psychosocial abilities following brain injury through intensive individual treatment which focuses on safety, skill building and increasing independence, community reintegration, and overall life satisfaction. Our treatment approach is two-fold, with emphasis not only on direct restoration of brain functions, but also on helping the individual learn compensatory strategies (e.g., internal mnemonics, organizational systems, self-cuing techniques) or acquire assistive devices (e.g., planners, electronic reminders). Such methods are designed to reduce the effects of real-world disability when there is enduring cognitive impairment, and are most effective when introduced within a person's own relevant environments.</p>
  </section>

  <section class="page page--right">
    <div class="section">
      <h2 class="section-title">Who We Serve</h2>
      <p class="statement">We treat adults and adolescents with a variety of diagnoses. We service home and community locations throughout Southeast and mid-Michigan.</p>
      <p class="statement">Our therapists hold a variety of certifications and endorsements including CBRS (Certified Brain Rehabilitation Specialist), SwallowSure, and VoiceBoost.</p>
    </div>
    <div class="diagnoses">
      <h4>Diagnoses can include:</h4>
      <ul class="check-list">
        <li><span class="tick tick--light"></span>Traumatic Brain Injury</li>
        <li><span class="tick tick--light"></span>Postconcussional Syndrome</li>
        <li><span class="tick tick--light"></span>Spinal Cord Injury</li>
        <li><span class="tick tick--light"></span>Post-traumatic Stress Disorder</li>
        <li><span class="tick tick--light"></span>Depression</li>
        <li><span class="tick tick--light"></span>Visual Impairments</li>
        <li><span class="tick tick--light"></span>Balance Disorders</li>
      </ul>
      <ul class="check-list">
        <li><span class="tick tick--light"></span>Anxiety</li>
        <li><span class="tick tick--light"></span>Mood Disorders</li>
        <li><span class="tick tick--light"></span>Musculoskeletal/Orthopedic injuries (ie. Spinal fractures/pathology, nerve injuries, pain)</li>
        <li><span class="tick tick--light"></span>Movement Disorders</li>
        <li><span class="tick tick--light"></span>Neuromuscular Pathologies</li>
        <li><span class="tick tick--light"></span>Dysphagia</li>
      </ul>
      <div class="funding">
        <h4>Funding Sources include:</h4>
        <ul class="check-list">
          <li><span class="tick tick--light"></span>No-Fault Auto Insurance</li>
          <li><span class="tick tick--light"></span>Workers Compensation Insurance</li>
          <li><span class="tick tick--light"></span>Some Commercial Health Insurance Carriers</li>
        </ul>
      </div>
    </div>
    <div class="section">
      <h2 class="section-title section-title--large">Services Offered</h2>
      <h3 class="sub-title">Speech Language Pathology</h3>
      <p>Speech &amp; Language Pathologists are trained in the rehabilitation of deficits/disorders in the areas of language, articulation, voice, fluency, and dysphagia, with an underlying knowledge base of the neurological and physiologic processes affecting each. Deficits in the areas of attention, memory, information processing and executive functioning can impact all of the areas that speech and language pathologists treat, and are addressed in all treatment goals.</p>
      <h3 class="sub-title">Services Include:</h3>
      <div class="services">
        <ul class="check-list">
          <li><span class="tick"></span>Immediate and Short-Term Memory: compensatory strategies, modification of the environment for increased functional memory.</li>
          <li><span class="tick"></span>Attention and concentration</li>
          <li><span class="tick"></span>Expressive Language: ability to express ideas, verbally, or in written format, in a concise organized fashion.</li>
          <li><span class="tick"></span>Comprehension and Retention of Verbal and Written Language</li>
          <li><span class="tick"></span>Information Processing: gradually increase in the length and complexity of information presented to allow the brain to take in and process more information at one time.</li>
        </ul>
        <ul class="check-list">
          <li><span class="tick"></span>Word Retrieval and Thought Formulation for Verbal and Written Expression</li>
          <li><span class="tick"></span>Pragmatic Language/Social Communication</li>
          <li><span class="tick"></span>Executive Functioning: The mental processes that enable individuals to plan, focus attention, retain instructions, and juggle multiple tasks successfully. Assist with planning, initiating, carrying out tasks, as well as assist with self-monitoring and awareness for carryover of strategies.</li>
          <li><span class="tick"></span>Articulation</li>
          <li><span class="tick"></span>Dysarthria (lack of voluntary control)</li>
          <li><span class="tick"></span>Dysphagia (swallowing disorders)</li>
          <li><span class="tick"></span>Voice</li>
        </ul>
      </div>
    </div>
    <div class="section">
      <h2 class="section-title section-title--large">Occupational Therapy</h2>
      <p>Occupational Therapists are experts at the evaluation and analysis of an individual's abilities relative to the demands of an activity and use this perspective in order to determine any aspects of the person's life that have been impacted, including activities of daily living (i.e., self-care), instrumental activities of daily living (i.e., home management, rest and sleep habits, work demands, play, leisure, and social participation). Treatment includes re-learning how to do activities (remediation) or determining new ways of accomplishing them (compensatory strategies).</p>
    </div>
  </section>
</main>
</body>
</html>
```